Artwork flyer ( named LO MI RA ) for my music festival

I need a flyer artwork created for my indie pop, rock, hip-hop and dance music festival as soon as possible. The festival is for ages 18 to 30. Need flyer to be able to be abstracted so i can export into different social media
sizes etc

Here is some information around the music festival details.

Title: LO MI RA ( music festival)

Artists :
PELI Fold
Moira Flint
KRTs
The Brellows
Zint Vobs
Tidal Baron
Velvet no
Amber Frost

Venue: Harrowby Paddock Club
Date: Saturday 25th March
Tickets: www.gatelyne.com.au

Logo Text

LOMI RA ( or LO MI RA)

```html
<!DOCTYPE html>
<html lang="en">
<head>
<meta charset="utf-8">
<title>LOMI RA Music Festival – Flyer</title>
<link rel="stylesheet" href="https://fonts.googleapis.com/css2?family=Montserrat:wght@500;600;700;800&display=swap">
<style>
  :root {
    --navy: #10295a;
    --navy-mid: #1d4a86;
    --cream: #fbf0da;
    --coral: #ef7458;
    --orange: #f49b2e;
    --sky: #3aa6c9;
    --stage: #e9e6e1;
  }
  * { margin: 0; padding: 0; box-sizing: border-box; }
  html, body { width: 1200px; height: 1200px; overflow: hidden; background: var(--stage); }
  body { font-family: "Montserrat", Arial, sans-serif; color: var(--navy); }

  .flyer {
    position: absolute; left: 200px; top: 35px;
    width: 800px; height: 1130px;
    background: var(--navy); overflow: hidden;
    box-shadow: 0 12px 30px rgba(0,0,0,.18);
  }
  .flyer-art { position: absolute; inset: 0; width: 800px; height: 1130px; }

  .content {
    position: absolute; left: 60px; top: 0; width: 640px;
    text-align: center;
  }
  .logo-name {
    margin-top: 120px;
    font-size: 112px; font-weight: 800; letter-spacing: 2px;
    color: var(--orange); line-height: 1;
  }
  .event-type {
    display: inline-block; margin-top: 22px;
    border: 2px solid var(--navy);
    padding: 8px 22px 8px 34px;
    font-size: 30px; font-weight: 600; letter-spacing: 14px;
  }
  .section-label {
    margin-top: 34px; font-size: 15px; font-weight: 600; letter-spacing: 7px;
  }
  .label-rule {
    width: 120px; margin: 8px auto 14px;
    border-top: 2px dotted var(--coral);
  }
  .artist-list {
    list-style: none; font-size: 33px; font-weight: 800; line-height: 1.24;
  }
  .artist-list .sep {
    display: inline-block; width: 12px; height: 12px; border-radius: 50%;
    background: var(--coral); margin: 0 10px; vertical-align: middle;
  }
  .event-info {
    display: flex; justify-content: center; align-items: center;
    gap: 22px; margin-top: 40px;
  }
  .event-date { text-align: right; color: var(--coral); font-weight: 800; font-size: 38px; line-height: 1; }
  .event-date .weekday { display: block; color: var(--navy); font-size: 20px; font-weight: 700; margin-top: 4px; }
  .info-divider { width: 0; height: 110px; border-left: 2px dotted var(--coral); }
  .event-venue { text-align: left; font-weight: 800; font-size: 34px; line-height: 1.02; }
  .tickets-label { margin-top: 34px; font-size: 17px; font-weight: 700; letter-spacing: 7px; }
  .ticket-url {
    display: inline-block; margin-top: 10px;
    background: var(--coral); color: var(--cream);
    font-size: 32px; font-weight: 800; letter-spacing: 1px;
    padding: 6px 20px;
  }
</style>
</head>
<body>
<main class="flyer">
  <svg class="flyer-art" viewBox="0 0 800 1130" aria-hidden="false">
    <defs>
      <linearGradient id="leafTone" x1="0" y1="0" x2="1" y2="1">
        <stop offset="0" stop-color="#2a5c9c"/>
        <stop offset="1" stop-color="#ef7458"/>
      </linearGradient>
      <linearGradient id="hornTone" x1="0" y1="0" x2="1" y2="1">
        <stop offset="0" stop-color="#ef7458"/>
        <stop offset=".5" stop-color="#f49b2e"/>
        <stop offset="1" stop-color="#2a5c9c"/>
      </linearGradient>
    </defs>

    <!-- side foliage illustrations -->
    <path role="img" aria-label="Illustrated coral and blue leaves" fill="url(#leafTone)" opacity=".55"
          d="M660 120 C760 160 800 260 790 360 C760 330 720 300 700 240 Z"/>
    <path role="img" aria-label="Illustrated blue leaves" fill="url(#leafTone)" opacity=".45"
          d="M0 330 C60 360 110 430 100 520 C60 480 20 440 0 400 Z"/>
    <path role="img" aria-label="Illustrated coral and blue leaves" fill="url(#leafTone)" opacity=".6"
          d="M80 900 C180 880 300 920 360 1010 C300 1060 180 1080 90 1040 C60 990 60 940 80 900 Z"/>

    <!-- cream content field -->
    <path class="content-field-outline" fill="none" stroke="#fbf0da" stroke-width="2"
          d="M-10 318 C40 380 60 450 80 530 C108 610 60 680 100 775 C140 868 210 898 322 938 C422 978 512 1028 552 1098 L720 1020 C700 980 668 920 680 845 C690 775 722 735 742 655 C762 575 762 485 732 415 C702 345 742 275 692 215 C642 155 702 75 664 -10"/>
    <path class="content-field" fill="#fbf0da"
          d="M0 0 H650 C690 60 630 140 680 200 C730 260 690 330 720 400 C750 470 750 560 730 640 C710 720 680 760 670 830 C660 900 690 960 710 1000 L560 1080 C520 1010 430 960 330 920 C220 880 150 850 110 760 C70 670 120 600 90 520 C60 440 40 360 0 300 Z"/>

    <!-- saxophone and splash illustration -->
    <path role="img" aria-label="Illustrated golden saxophone bursting with splashes and leaves"
          fill="url(#hornTone)"
          d="M470 1000 C520 930 600 880 660 820 C700 780 740 760 790 770 L800 1130 H430 C420 1080 440 1040 470 1000 Z"/>

    <!-- scattered dots -->
    <g class="confetti">
      <circle cx="40" cy="460" r="6" fill="#f49b2e"/>
      <circle cx="770" cy="470" r="6" fill="#f49b2e"/>
      <circle cx="745" cy="640" r="7" fill="#ef7458"/>
      <circle cx="60" cy="780" r="5" fill="#f49b2e"/>
      <circle cx="240" cy="1060" r="7" fill="#ef7458"/>
      <circle cx="140" cy="1100" r="5" fill="#f49b2e"/>
      <circle cx="30" cy="620" r="5" fill="#3aa6c9"/>
      <circle cx="780" cy="300" r="5" fill="#ef7458"/>
    </g>
  </svg>

  <section class="content">
    <h1 class="logo-name">LOMI RA</h1>
    <div class="event-type">MUSIC FESTIVAL</div>

    <p class="section-label">ARTISTS</p>
    <div class="label-rule"></div>
    <ul class="artist-list">
      <li>PELI FOLD<span class="sep"></span>MOIRA FLINT</li>
      <li>KRTS<span class="sep"></span>THE BRELLOWS<span class="sep"></span>ZINT VOBS</li>
      <li>TIDAL BARON<span class="sep"></span>VELVET NO</li>
      <li>AMBER FROST</li>
    </ul>

    <div class="event-info">
      <p class="event-date">25TH<br>MARCH<span class="weekday">SATURDAY</span></p>
      <div class="info-divider"></div>
      <p class="event-venue">HARROWBY<br>PADDOCK<br>CLUB</p>
    </div>

    <p class="tickets-label">TICKETS</p>
    <p class="ticket-url">WWW.GATELYNE.COM.AU</p>
  </section>
</main>
</body>
</html>
```